Classy website for Corporate Entertainment - Action & Acrobatic Shows

12-Page Website to be coded using Wordpress!

We are "Velvet Summit Productions". We are all about providing 'experiences'! This website must be part of that experience :)

Please do not use our current website as inspiration for your design! We are looking for something new, and our business has outgrown that site (which was just for our shows) :)

We perform Action & Acrobatic Shows for corporate functions, as well as run Classes & Workshops from our Training Centre (Parkour, Acrobatics, etc), as well as Client Action Experiences and other services.

Example of our recent Morgan Vale 'Acrobatic Action Show' https://clipvault.example/watch/QxTr7nLpWzK

Our website must be super-classy/suave!! Needs to be heavily appealing to the Corporate community!

www.friendsphere.example/velvetsummitlive

Logo is available in the files below.
A series of photos have also been uploaded; please use any of these that you like throughout the design.

Menu Links from Home Page:
About Us (dropdown), Corporate Action Shows, Services (dropdown), Classes & Workshops (dropdown), The Ultimate Action Experience, Blog, Photos/Videos, Contact Us

PAGES:
- Home Page - must include a focus on Corporate Entertainment for the first glance, with information going down the page about our 4 major aspects: our Corporate Action Shows, Workshops & Classes, Services and Blog.

Required links on menu (menu does not necessarily have to be as a banner across the top - we are open to all ideas):

- Home Page

-"About Us" (dropdown with x2 pages "Our Shows" and "Our Team")

- Corporate Action Shows (x1 page)

- Services (dropdown with x3 pages "Action Showreels", and "Cosplay Competition Skits", and "Film & TV"

- Classes & Workshops (dropdown with x2 pages "Class Details & Prices" and "2016 Timetable"

- Ultimate Action Experience (x1 page with link to external website)

- Blog

- Videos & Photos or "See Us In Action" (x1 page)

- Contact Us

If you need more in-depth information into anything, please do not hesitate to send us a message!

Target Market(s)

Corporate (Classy)

Industry/Entity Type

Entertainment

Coding

Coded - Design and coding required

Number of Pages Required

5+ page

Requirements
Must have
• Website Coded via Wordpress

```html
<!DOCTYPE html>
<html lang="en">
<head>
<meta charset="utf-8">
<title>Velvet Summit Productions</title>
<link rel="stylesheet" href="https://fonts.googleapis.com/css2?family=Raleway:ital,wght@0,300;0,400;0,500;0,600;0,700;0,800;1,400&family=Open+Sans:wght@400;600&display=swap">
<style>
  :root {
    --white: #ffffff;
    --ink: #1f1f1f;
    --body: #3a3a3a;
    --muted: #7a7a7a;
    --teal: #1abc9c;
    --footer: #222222;
    --footer-base: #0f0f0f;
    --footer-text: #e6e6e6;
    --footer-muted: #9a9a9a;
    --photo-warm: #7a1a3a;
    --photo-dusk: #4a4038;
    --avatar: #5a4a44;
    --social-1: #3b5998;
    --social-2: #1da1d8;
    --social-3: #e3185a;
    --social-4: #0f4f8a;
    --social-5: #f0862e;
  }
  * { margin: 0; padding: 0; box-sizing: border-box; }
  html, body { width: 1200px; height: 900px; overflow: hidden; }
  body { position: relative; background: var(--white); font-family: "Raleway", sans-serif; color: var(--ink); }

  .section-title { position: absolute; top: 16px; font-size: 29px; font-weight: 800; letter-spacing: 0.2px; color: var(--ink); }
  .testimonials-title { left: 167px; }
  .blog-title { left: 627px; }

  .avatar { position: absolute; left: 178px; width: 50px; height: 50px; border-radius: 50%; background: radial-gradient(circle at 50% 40%, #a08a80, var(--avatar) 70%); }
  .quote { position: absolute; left: 249px; width: 200px; font-size: 14.5px; font-style: italic; line-height: 20.7px; color: var(--body); }
  .quote-author { position: absolute; left: 250px; font-size: 14px; font-weight: 700; color: var(--ink); }

  .post-image { position: absolute; left: 627px; width: 158px; height: 119px; }
  .post-image.event { top: 83px; background: linear-gradient(160deg, #e0306a 0%, var(--photo-warm) 45%, #150508 100%); }
  .post-image.meetup { top: 252px; background: linear-gradient(180deg, #6a6a70 0%, var(--photo-dusk) 45%, #f0b040 70%, #1a140e 85%); }
  .post-category { position: absolute; left: 812px; font-size: 13px; font-weight: 300; color: var(--muted); }
  .post-title { position: absolute; left: 812px; width: 260px; font-size: 18px; font-weight: 300; line-height: 21px; color: var(--ink); }
  .read-more { position: absolute; font-family: "Open Sans", sans-serif; font-size: 11px; font-weight: 600; color: var(--teal); text-decoration: none; border-bottom: 1px solid var(--teal); line-height: 13px; }

  .site-footer { position: absolute; left: 0; top: 461px; width: 1200px; height: 361px; background: var(--footer); color: var(--footer-text); }
  .brand { position: absolute; left: 164px; top: 74px; display: flex; align-items: center; gap: 6px; }
  .brand-mark { width: 34px; height: 34px; border: 2px solid var(--white); }
  .brand-name { font-size: 12px; font-weight: 800; line-height: 12px; letter-spacing: 0.8px; text-transform: uppercase; color: var(--white); width: 70px; }
  .footer-nav { position: absolute; left: 168px; top: 141px; list-style: none; }
  .footer-nav li { font-size: 10px; letter-spacing: 0.6px; text-transform: uppercase; line-height: 23px; color: var(--footer-text); }

  .footer-heading { position: absolute; top: 84px; font-size: 16px; font-weight: 400; letter-spacing: 1.4px; text-transform: uppercase; color: var(--footer-text); }
  .newsletter-heading { left: 459px; }
  .contact-heading { left: 842px; }
  .email-field { position: absolute; left: 463px; top: 146px; width: 269px; height: 39px; background: var(--white); font-size: 16px; font-weight: 300; color: #a8a8a8; text-align: center; line-height: 39px; }
  .subscribe-button { position: absolute; left: 520px; top: 200px; width: 151px; height: 37px; background: var(--teal); color: var(--white); font-size: 12.5px; font-weight: 700; letter-spacing: 1.3px; text-transform: uppercase; text-align: center; line-height: 37px; }

  .address { position: absolute; left: 841px; top: 122px; font-size: 13.5px; font-weight: 400; line-height: 21px; color: var(--footer-text); }
  .call { position: absolute; left: 841px; top: 176px; font-size: 13px; letter-spacing: 0.5px; color: var(--footer-text); }
  .call strong { margin-left: 10px; font-size: 16px; font-weight: 800; letter-spacing: 0.6px; color: var(--white); }
  .social-links { position: absolute; left: 841px; top: 214px; display: flex; gap: 7px; list-style: none; }
  .social-links li { width: 29px; height: 29px; }
  .social-links li:nth-child(1) { background: var(--social-1); }
  .social-links li:nth-child(2) { background: var(--social-2); }
  .social-links li:nth-child(3) { background: var(--social-3); }
  .social-links li:nth-child(4) { background: var(--social-4); }
  .social-links li:nth-child(5) { background: var(--social-5); }

  .footer-base { position: absolute; left: 0; top: 822px; width: 1200px; height: 78px; background: var(--footer-base); }
  .copyright { text-align: center; padding-top: 32px; font-size: 11.5px; font-weight: 400; color: var(--footer-muted); }
</style>
</head>
<body>
  <section class="testimonials">
    <h2 class="section-title testimonials-title">TESTIMONIALS</h2>

    <div class="avatar" style="top:138px" role="img" aria-label="Portrait photo of a client"></div>
    <p class="quote" style="top:108px">Mauris elit justo, molestie sed purus eu, porttitor rutrum massa. Cras elemen-tum sollicitudin metus</p>
    <p class="quote-author" style="top:206px">CEO Company LTD.</p>

    <div class="avatar" style="top:299px" role="img" aria-label="Portrait photo of a client"></div>
    <p class="quote" style="top:273px">Mauris elit justo, molestie sed purus eu, porttitor rutrum massa. Cras elemen-tum sollicitudin metus</p>
    <p class="quote-author" style="top:371px">CEO Company LTD.</p>
  </section>

  <section class="blog">
    <h2 class="section-title blog-title">LATEST BLOG POSTS</h2>

    <div class="post-image event" role="img" aria-label="Photo of a crowded ballroom event under pink stage lights"></div>
    <p class="post-category" style="top:87px">Performances</p>
    <h3 class="post-title" style="top:113px">Amazing Event for Company's 50th birthday</h3>
    <a class="read-more" href="#" style="left:810px;top:182px">Read more</a>

    <div class="post-image meetup" role="img" aria-label="Photo of two sword fighters silhouetted against a sunset"></div>
    <p class="post-category" style="top:260px">Press &amp; Media</p>
    <h3 class="post-title" style="top:286px;line-height:23px">Global Meetup Program is Launching!</h3>
    <a class="read-more" href="#" style="left:813px;top:353px">Read more</a>
  </section>

  <footer class="site-footer">
    <div class="brand">
      <span class="brand-mark"></span>
      <span class="brand-name">Velvet Summit Productions</span>
    </div>
    <ul class="footer-nav">
      <li>About</li>
      <li>Corporate Action Shows</li>
      <li>Services</li>
      <li>Classes &amp; Workshops</li>
      <li>Ultimate Action Experience</li>
      <li>See Us In Action</li>
    </ul>

    <h3 class="footer-heading newsletter-heading">Subscribe to our newsletter</h3>
    <div class="email-field">Your Email Address</div>
    <div class="subscribe-button">Subscribe Now</div>

    <h3 class="footer-heading contact-heading">Contact</h3>
    <p class="address">418 Larkspur Ave, Suite 210<br>Millbrook, CA 94032</p>
    <p class="call">CALL <strong>0400-555-018</strong></p>
    <ul class="social-links" aria-label="Social links">
      <li></li><li></li><li></li><li></li><li></li>
    </ul>
  </footer>

  <div class="footer-base">
    <p class="copyright">Copyright VELVET / SUMMIT 2016 | All Rights Reserved</p>
  </div>
</body>
</html>
```